Changes to an existing brochure needed

We need to make some changed to an existing product brochure to add more localised information in it and to make it looks better.

We have set out in a pdf file where needs to be changed. Apart from that, any changes on the design of the brochure that can make the brochure looks better will be appreciated.

Target Market(s)

Technology market

Industry/Entity Type

Technology Equipment

Colors

Designer to choose colors to be used in the design.

Requirements
Must have
• The content outlined in the pdf file.
Nice to have
• Some creative designs that can make the brochure looks better and more professional.
Should not have
• N/A

```html
<!DOCTYPE html>
<html lang="en">
<head>
<meta charset="utf-8">
<title>Filament Range Brochure</title>
<link href="https://fonts.googleapis.com/css2?family=Roboto+Condensed:wght@400;700&display=swap" rel="stylesheet">
<style>
:root{
  --teal:#1ba57c;
  --teal-dark:#0f6f4e;
  --panel-mid-a:#2c7c5f;
  --panel-mid-b:#5fbf98;
  --ink:#222;
  --white:#fff;
  --orange:#f6ad3c;
  --band-left:#3a9a76;
}
*{box-sizing:border-box;margin:0;padding:0}
html,body{width:1200px;height:400px;overflow:hidden;background:#fff}
body{font-family:"Roboto Condensed",Arial,sans-serif;color:var(--ink)}
.brochure{position:relative;width:1200px;height:400px;overflow:hidden}
.panel{position:absolute;top:0;height:400px}
.panel--left{left:0;width:400px;background:linear-gradient(160deg,#fff,#f2f2f2 60%,#fff)}
.panel--mid{left:400px;width:400px;background:linear-gradient(160deg,var(--panel-mid-a),var(--panel-mid-b))}
.panel--right{left:800px;width:400px;background:linear-gradient(160deg,#fff,#f3f3f3 60%,#fff)}

.card{position:absolute;width:170px;height:48px}
.thumb{position:absolute;top:0;left:0;width:49px;height:48px;border:1px solid var(--teal);background:#ddd}
.card--flip .thumb{left:auto;right:0}
.band{position:absolute;top:0;left:49px;width:121px;height:14px;background:var(--teal);
  clip-path:polygon(0 0,88% 0,100% 100%,0 100%);color:var(--white);font-weight:700;
  font-size:12.5px;line-height:14px;padding-left:4px;white-space:nowrap;letter-spacing:.2px;overflow:hidden}
.card--flip .band{left:0;clip-path:polygon(12% 0,100% 0,100% 100%,0 100%);text-align:right;padding:0 4px 0 0}
.panel--mid .band{background:var(--teal-dark)}
.points{position:absolute;top:15px;left:53px;right:0;list-style:none;font-size:7.3px;line-height:10px}
.card--flip .points{left:0;right:53px;text-align:right}
.panel--mid .points{color:var(--white)}
.points li::before{content:"• "}
.points .cont::before{content:"";padding-left:6px}

.stay{position:absolute;left:1009px;top:181px;width:170px;height:48px}
.stay .band{left:0;width:126px;height:32px;top:0;clip-path:polygon(12% 0,100% 0,100% 100%,0 100%);
  text-align:right;font-size:12.5px;line-height:15px;padding:1px 4px 0 0;white-space:normal}
.stay .box{position:absolute;right:0;top:0;width:49px;height:48px;border:1px solid var(--teal);background:#fff}

.swatches{position:absolute;left:821px;top:233px;display:grid;grid-template-columns:repeat(9,35px);
  column-gap:5.5px;row-gap:5px;list-style:none}
.swatch{width:35px;height:40px;border:1px solid var(--teal);position:relative;overflow:hidden}
.swatch span{position:absolute;bottom:0;left:0;right:0;height:6px;background:var(--teal);color:#fff;
  font-size:4px;line-height:6px;text-align:center;white-space:nowrap}

.footer{position:absolute;top:367px;height:29px;font-weight:700;color:#fff;font-size:8px;line-height:29px;padding-left:21px}
.footer--left{left:0;width:400px;background:linear-gradient(90deg,var(--band-left),#4bb88e)}
.footer--right{left:800px;width:400px;background:var(--orange);font-size:9.5px;letter-spacing:.3px}
.strip{position:absolute;top:396px;height:4px}
.strip--l{left:0;width:400px;background:var(--teal)}
.strip--m{left:400px;width:400px;background:var(--orange)}
.strip--r{left:800px;width:400px;background:var(--teal)}
</style>
</head>
<body>
<main class="brochure">
  <section class="panel panel--left">
    <article class="card" style="left:21px;top:21px">
      <div class="thumb" role="img" aria-label="Printed rose" style="background:linear-gradient(160deg,#f3c4cc,#d9657a)"></div>
      <h2 class="band">PLA/PLA+</h2>
      <ul class="points"><li>Environmental-friendly material.</li><li>High print quality.</li><li>Good strength.</li></ul>
    </article>
    <article class="card" style="left:208px;top:21px">
      <div class="thumb" role="img" aria-label="Low-poly cat model" style="background:linear-gradient(160deg,#555,#1e1e1e)"></div>
      <h2 class="band">ABS/ABS+</h2>
      <ul class="points"><li>High strength.</li><li>Good toughness.</li><li>Low shrinkage for ABS+.</li></ul>
    </article>
    <article class="card card--flip" style="left:21px;top:91px">
      <div class="thumb" role="img" aria-label="Jet model" style="background:linear-gradient(160deg,#fafafa,#cfcfcf)"></div>
      <h2 class="band">ABS-HT</h2>
      <ul class="points"><li>Good temperature tolerance</li><li class="cont">and creep resistance.</li><li>Flame retardant.</li></ul>
    </article>
    <article class="card card--flip" style="left:208px;top:91px">
      <div class="thumb" role="img" aria-label="Car model" style="background:linear-gradient(160deg,#f4f4f4,#3a3a3a)"></div>
      <h2 class="band">ASA UV</h2>
      <ul class="points"><li>Excellent mechanical property.</li><li>Outstanding UV-resistance.</li></ul>
    </article>
    <article class="card" style="left:21px;top:161px">
      <div class="thumb" role="img" aria-label="Translucent printed bells" style="background:linear-gradient(160deg,#f4d24a,#e23a3a)"></div>
      <h2 class="band">PETG</h2>
      <ul class="points"><li>Low shrinkage.</li><li>Good toughness.</li><li>High transparency and gloss.</li></ul>
    </article>
    <article class="card" style="left:208px;top:161px">
      <div class="thumb" role="img" aria-label="Printed figures with support" style="background:linear-gradient(160deg,#f2f2f2,#c9343b)"></div>
      <h2 class="band">PVA</h2>
      <ul class="points"><li>Water soluble material.</li><li>Ideal for support structure.</li></ul>
    </article>
    <article class="card card--flip" style="left:21px;top:231px">
      <div class="thumb" role="img" aria-label="Patterned cat figure" style="background:linear-gradient(160deg,#e9eef8,#3a79c9)"></div>
      <h2 class="band">HIPS</h2>
      <ul class="points"><li>Soluble in Limonence.</li><li>Works well with ABS.</li></ul>
    </article>
    <article class="card card--flip" style="left:208px;top:231px">
      <div class="thumb" role="img" aria-label="Translucent bottles" style="background:linear-gradient(160deg,#f2f2ee,#b8d7a0)"></div>
      <h2 class="band">PC Pro</h2>
      <ul class="points"><li>High distortion temperature.</li><li>Low flammability.</li></ul>
    </article>
    <article class="card" style="left:21px;top:301px">
      <div class="thumb" role="img" aria-label="Lit printed lantern" style="background:radial-gradient(circle at 50% 60%,#f0a21c,#1a1409 70%)"></div>
      <h2 class="band">PA (Nylon)</h2>
      <ul class="points"><li>High toughness.</li><li>Outstanding chemical</li><li class="cont">resistance.</li></ul>
    </article>
    <article class="card" style="left:208px;top:301px">
      <div class="thumb" role="img" aria-label="Carbon fibre tool parts" style="background:linear-gradient(160deg,#fafafa,#d0d0d0)"></div>
      <h2 class="band">PA-CF Rigid</h2>
      <ul class="points"><li>20% carbon fibre.</li><li>Highly rigid.</li><li>Good toughness and wear-resistance.</li></ul>
    </article>
    <div class="footer footer--left">Multicolor Filament: PLA, PLA+, ABS, ABS+, PETG, HIPS, PCL, COLOR CHANGE, Resin Series......</div>
  </section>

  <section class="panel panel--mid">
    <article class="card" style="left:21px;top:21px">
      <div class="thumb" role="img" aria-label="Copper-finish vases" style="background:linear-gradient(160deg,#f3efe9,#8e4a2c)"></div>
      <h2 class="band">Copper Fill</h2>
      <ul class="points"><li>Easy to process.</li><li>Metal texture after polishing.</li></ul>
    </article>
    <article class="card" style="left:208px;top:21px">
      <div class="thumb" role="img" aria-label="Bronze ingot models" style="background:linear-gradient(160deg,#eeeee6,#a59a55)"></div>
      <h2 class="band">Bronze</h2>
      <ul class="points"><li>Easy to print.</li><li>Nice shiny finish.</li></ul>
    </article>
    <article class="card card--flip" style="left:21px;top:97px">
      <div class="thumb" role="img" aria-label="Aluminium-filled prints" style="background:linear-gradient(160deg,#f0f0f0,#6e6e6e)"></div>
      <h2 class="band">Alu Fill</h2>
      <ul class="points"><li>Aluminium filled PLA filament.</li><li>Metal texture after polishing.</li></ul>
    </article>
    <article class="card card--flip" style="left:208px;top:97px">
      <div class="thumb" role="img" aria-label="Steel-finish statue" style="background:linear-gradient(160deg,#f4f4f4,#5a5a5a)"></div>
      <h2 class="band">Steel Fill</h2>
      <ul class="points"><li>Stainless steel filled PLA filament.</li><li>Metal texture after polishing.</li></ul>
    </article>
    <article class="card" style="left:21px;top:173px">
      <div class="thumb" role="img" aria-label="Cleaning filament instructions" style="background:linear-gradient(160deg,#dfe3e8,#9fb0c3)"></div>
      <h2 class="band">Purge</h2>
      <ul class="points"><li>Cleaning extruder before</li><li class="cont">or after prints.</li><li>Wide printing temperature range.</li></ul>
    </article>
    <article class="card" style="left:208px;top:173px">
      <div class="thumb" role="img" aria-label="Colour-changing prints outdoors" style="background:linear-gradient(160deg,#6aa84f,#d2589a)"></div>
      <h2 class="band">Color Change</h2>
      <ul class="points"><li>Color changing by UV or</li><li class="cont">temperature.</li><li>Reversible color change.</li></ul>
    </article>
    <article class="card card--flip" style="left:21px;top:249px">
      <div class="thumb" role="img" aria-label="Wood-finish animal print" style="background:linear-gradient(160deg,#fbf7f1,#d9b98c)"></div>
      <h2 class="band">Wood</h2>
      <ul class="points"><li>Wood texture finish.</li><li>Low warping.</li></ul>
    </article>
    <article class="card card--flip" style="left:208px;top:249px">
      <div class="thumb" role="img" aria-label="Bamboo-finish pagoda" style="background:linear-gradient(160deg,#fbfbfb,#9a4a25)"></div>
      <h2 class="band">Bamboo Fill</h2>
      <ul class="points"><li>Matte finish with dark</li><li class="cont">bamboo colour.</li><li>Print with wood aroma.</li></ul>
    </article>
    <article class="card" style="left:21px;top:325px">
      <div class="thumb" role="img" aria-label="Flexible insoles" style="background:linear-gradient(160deg,#2f6f7c,#9ccf6a)"></div>
      <h2 class="band">TPU / TPE Flex</h2>
      <ul class="points"><li>High flexibility.</li><li>Good resilience.</li></ul>
    </article>
    <article class="card" style="left:208px;top:325px">
      <div class="thumb" role="img" aria-label="Hand squeezing flexible print" style="background:linear-gradient(160deg,#f8f8f8,#d9c3b3)"></div>
      <h2 class="band">Soft TPU Lite</h2>
      <ul class="points"><li>Cost effective flexible material.</li><li>Good dimensional stability.</li></ul>
    </article>
  </section>

  <section class="panel panel--right">
    <article class="card" style="left:21px;top:21px">
      <div class="thumb" role="img" aria-label="Smooth white sphere" style="background:radial-gradient(circle,#f3efe4,#fff 70%)"></div>
      <h2 class="band">Smooth Cast</h2>
      <ul class="points"><li>Can be polished by alcohol.</li><li>Great material for metal casting.</li></ul>
    </article>
    <article class="card" style="left:209px;top:21px">
      <div class="thumb" role="img" aria-label="Pen-drawn figures" style="background:linear-gradient(160deg,#fffbe6,#f2d31b)"></div>
      <h2 class="band">PCL Low-Temp</h2>
      <ul class="points"><li>FDA approved material.</li><li>Low melting temperature.</li><li>Ideal for both 3D printer and 3D pen.</li></ul>
    </article>
    <article class="card card--flip" style="left:21px;top:75px">
      <div class="thumb" role="img" aria-label="Red resin tower and ball" style="background:linear-gradient(160deg,#fff,#e3262e)"></div>
      <h2 class="band">Bio Resin</h2>
      <ul class="points"><li>Environmental-friendly.</li><li>Solidified by both UV and</li><li class="cont">visible light.</li></ul>
    </article>
    <article class="card card--flip" style="left:209px;top:75px">
      <div class="thumb" role="img" aria-label="Green resin jewellery models" style="background:linear-gradient(160deg,#f4f7e8,#9fd23a)"></div>
      <h2 class="band">Cast Resin</h2>
      <ul class="points"><li>High precision.</li><li>Smooth surface.</li><li>Ideal for metal casting.</li></ul>
    </article>
    <article class="card" style="left:21px;top:128px">
      <div class="thumb" role="img" aria-label="Orange resin lattice print" style="background:linear-gradient(160deg,#7fa9c9,#d98a2b)"></div>
      <h2 class="band">Fast Resin</h2>
      <ul class="points"><li>Fast printing speed.</li><li>Low shrinkage.</li></ul>
    </article>
    <article class="card" style="left:209px;top:128px">
      <div class="thumb" role="img" aria-label="Dental resin model" style="background:linear-gradient(160deg,#7fa0b8,#f0c9b5)"></div>
      <h2 class="band">Dental Resin</h2>
      <ul class="points"><li>Special designed for dental purpose.</li><li>High precision.</li><li>Good hardness.</li></ul>
    </article>
    <article class="card card--flip" style="left:21px;top:181px">
      <div class="thumb" role="img" aria-label="Printed boat benchmark" style="background:linear-gradient(160deg,#fff,#c9ab9a)"></div>
      <h2 class="band">PEEK</h2>
      <ul class="points"><li>Outstanding mechanical properties.</li><li>High strength, wear and</li><li class="cont">fatigue resistance.</li></ul>
    </article>
    <div class="stay"><h2 class="band">Stay tuned for<br>more materials</h2><div class="box"></div></div>
  </section>

  <ul class="swatches" aria-label="Available colours">
    <li class="swatch" style="background:linear-gradient(#f7f4fa,#d9d3e6)"><span>White</span></li>
    <li class="swatch" style="background:linear-gradient(#f6f7ec,#e3e6cc)"><span>Luminous Green</span></li>
    <li class="swatch" style="background:linear-gradient(#f3f0ea,#ddd6c8)"><span>Natural</span></li>
    <li class="swatch" style="background:linear-gradient(#fbe6e0,#eec2b4)"><span>Skin</span></li>
    <li class="swatch" style="background:linear-gradient(#fff7a8,#f2e21b)"><span>Yellow</span></li>
    <li class="swatch" style="background:linear-gradient(#fcd79a,#eda52a)"><span>Gold</span></li>
    <li class="swatch" style="background:linear-gradient(#fcc3a4,#f1763a)"><span>Orange</span></li>
    <li class="swatch" style="background:linear-gradient(#fcc4d8,#f0709e)"><span>Luminous Red</span></li>
    <li class="swatch" style="background:linear-gradient(#e9ebe8,#b9bdb7)"><span>Luminous Blue</span></li>
    <li class="swatch" style="background:linear-gradient(#fbb4c6,#ee5a82)"><span>Pink</span></li>
    <li class="swatch" style="background:linear-gradient(#f79ab8,#e0306b)"><span>Magenta</span></li>
    <li class="swatch" style="background:linear-gradient(#f08a8a,#d9202b)"><span>Red</span></li>
    <li class="swatch" style="background:linear-gradient(#d67cb8,#9b1a78)"><span>Glass Purple</span></li>
    <li class="swatch" style="background:linear-gradient(#f6e690,#e0c22a)"><span>Glass Lemon</span></li>
    <li class="swatch" style="background:linear-gradient(#f8c77a,#e98d18)"><span>Glass Orange</span></li>
    <li class="swatch" style="background:linear-gradient(#f58a8a,#d6252d)"><span>Glass Red</span></li>
    <li class="swatch" style="background:linear-gradient(#b58ad6,#6a2aa5)"><span>Purple</span></li>
    <li class="swatch" style="background:linear-gradient(#b8b9d4,#6d6f9c)"><span>Gray</span></li>
    <li class="swatch" style="background:linear-gradient(#c9efc0,#8fd88a)"><span>Peak Green</span></li>
    <li class="swatch" style="background:linear-gradient(#bfeef6,#56c8e0)"><span>Light Blue</span></li>
    <li class="swatch" style="background:linear-gradient(#8fcaa3,#1f8049)"><span>Pine Green</span></li>
    <li class="swatch" style="background:linear-gradient(#7fc3c8,#137c86)"><span>Green</span></li>
    <li class="swatch" style="background:linear-gradient(#8a99ea,#1d33c6)"><span>Blue</span></li>
    <li class="swatch" style="background:linear-gradient(#9ab4ef,#2c5ad6)"><span>Glass Light Blue</span></li>
    <li class="swatch" style="background:linear-gradient(#c09a86,#6e3a22)"><span>Brown</span></li>
    <li class="swatch" style="background:linear-gradient(#8f8a9a,#2a2730)"><span>Black</span></li>
    <li class="swatch" style="background:linear-gradient(#eeeeee,#bdbdbd)"><span>Silver</span></li>
  </ul>

  <div class="footer footer--right">Please email orders@filamentstore.example for more product information.</div>
  <div class="strip strip--l"></div><div class="strip strip--m"></div><div class="strip strip--r"></div>
</main>
</body>
</html>
```